Postcard Design

Looking for 4.25 x6 postcard design for mass mailing
Design should be eye catching, energetic and draw the viewer in

Data for postcard to include:
Logo and slogan
Pediatric Occupational, Physical and Speech Therapy Services; Assistive Technology Evaluation and Training

Speech-Language Therapy
oral motor skills
speech delays
language skills
Articulation
Voice
fluency
cognitive skills
feeding disorders
Play skills

OCCUPATIONAL THERAPY
Our occupational therapists use play in therapy to help your child develop the skills he/she needs to perform their job of living and playing, including but not limited to:
- Increasing independence in self-care skills such as feeding, dressing and grooming
- Improving developmental skills such as rolling, sitting, standing
- Improving their sensory processing, balance, coordination and motor planning
- Difficulty tolerating clothing
- Poor balance - doesn't ride a bike/climb on slides, falls frequently, cries when moved unexpectedly
- Intolerance to textures/odors/loud sounds/movement
- Delayed handwriting and fine motor skills and/or
avoids fine motor activities such as using crayons, fasteners on clothing, pencils
- Limited diet-refuses to try new foods, gags when trying new tastes, textures
- Appears extremely anxious, states frequent fears of harmless things

CONTACT US TODAY for a FREE 15 minute consultation/Screen
(301) 555-4182
info@brightwillowkids.example
www.brightwillowkids.example

Physical therapy
Delayed crawling / walking
Persistent toe walking habits
Poor unsupported sitting/standing balance
Trouble learning how to jump, skip, ride a bike
Decreased ability to throw and catch a ball
Delayed motor milestones
Need for wheelchair mobility training
Balance coordination and motor planning difficulty
Strength , muscle tone and/ R range of motion impairment
Sports injuries
Postural control and positioning difficulty

```html
<!DOCTYPE html>
<html lang="en">
<head>
<meta charset="utf-8">
<title>Bright Willow Kids – Postcard</title>
<link href="https://fonts.googleapis.com/css2?family=Fira+Sans:ital,wght@0,400;0,600;0,700;1,400&family=Fira+Sans+Extra+Condensed:wght@400&display=swap" rel="stylesheet">
<style>
  :root {
    --bg: #7a7a7a;
    --paper: #ffffff;
    --teal: #13948c;
    --navy: #1d5e9e;
    --band: #0c75c6;
    --ink: #3a3a3a;
    --icon: #f2c230;
    --rule: #9a9a9a;
  }
  * { box-sizing: border-box; margin: 0; padding: 0; }
  html, body { width: 1200px; height: 904px; overflow: hidden; }
  body { background: var(--bg); position: relative; font-family: "Fira Sans", sans-serif; color: var(--ink); }

  .card { position: absolute; width: 513px; height: 364px; background: var(--paper); overflow: hidden; box-shadow: 0 3px 8px rgba(0,0,0,.25); }
  .card--front { left: 154px; top: 73px; background: linear-gradient(180deg, #f1f2f3, #e6e8ea); }
  .card--back { left: 552px; top: 464px; }

  .tick { width: 8px; height: 8px; flex: none; }

  /* brand */
  .brand { position: absolute; display: flex; align-items: center; gap: 6px; }
  .brand__dot { width: 14px; height: 14px; border-radius: 50%; background: var(--teal); }
  .brand__name { font-weight: 600; color: var(--navy); }
  .brand__slogan { position: absolute; font-style: italic; color: var(--navy); }

  /* front */
  .front__photo { position: absolute; left: 235px; top: 0; width: 278px; height: 324px;
    background: radial-gradient(ellipse at 55% 50%, #6b6b6b 0%, #9a9a9a 45%, #d9dadb 80%, rgba(230,232,234,0) 100%); }
  .front__headline { position: absolute; left: 31px; top: 86px; width: 240px; font-size: 15.6px; line-height: 19.5px; font-weight: 700; letter-spacing: -.1px; }
  .front__headline .teal { color: var(--teal); }
  .front__headline .navy { color: var(--navy); }
  .front__subhead { position: absolute; left: 31px; top: 181px; font-size: 11.3px; font-weight: 700; color: var(--navy); }
  .skill-list { position: absolute; top: 200px; list-style: none; font-size: 10.3px; color: #333; }
  .skill-list li { display: flex; align-items: center; gap: 5px; height: 16.8px; }
  .skill-list--a { left: 31px; }
  .skill-list--b { left: 135px; }
  .cta { position: absolute; font-weight: 700; }
  .cta__lead { color: var(--navy); display: block; }
  .cta__offer { color: var(--teal); display: block; }
  .front .cta { left: 31px; top: 293px; font-size: 10px; line-height: 13px; }

  .contact-band { position: absolute; left: 0; background: var(--band); color: #fff; }
  .contact-item { display: flex; align-items: center; gap: 4px; white-space: nowrap; }
  .contact-item svg { width: 10px; height: 10px; flex: none; }
  .front .contact-band { top: 324px; width: 513px; height: 40px; display: flex; align-items: center; gap: 23px; padding-left: 30px; font-size: 10.6px; }
  .front .contact-item:first-child { font-weight: 600; }

  /* back */
  .back__divider { position: absolute; left: 275px; top: 0; width: 2px; height: 364px; background: var(--teal); }
  .section-tab { position: absolute; left: 0; top: 27px; width: 167px; height: 17px; background: var(--teal); border-radius: 0 9px 9px 0; color: #fff; font-weight: 700; font-size: 10px; line-height: 17px; padding-left: 30px; letter-spacing: .1px; }
  .back__intro, .ot-list { font-family: "Fira Sans Extra Condensed", sans-serif; font-size: 7.4px; line-height: 11.3px; color: #444; }
  .back__intro { position: absolute; left: 30px; top: 46px; width: 233px; text-align: justify; }
  .ot-list { position: absolute; left: 30px; top: 86px; width: 233px; list-style: none; }
  .ot-list li { display: flex; gap: 5px; margin-bottom: 5px; text-align: justify; }
  .ot-list li:last-child { margin-bottom: 0; }
  .ot-list .tick { width: 6.5px; height: 6.5px; margin-top: 2px; }
  .back .cta { left: 30px; top: 288px; font-size: 10px; line-height: 13px; }
  .back .contact-band { top: 317px; width: 275px; height: 47px; padding: 5px 0 0 30px; font-size: 9.2px; }
  .back .contact-band .row { display: flex; gap: 20px; height: 15px; align-items: center; }

  .stamp-box { position: absolute; left: 440px; top: 30px; width: 47px; height: 47px; border: 1.5px solid #888; }
  .address-line { position: absolute; left: 297px; width: 190px; height: 1px; background: var(--rule); }
</style>
</head>
<body>
<svg width="0" height="0" style="position:absolute">
  <defs>
    <symbol id="tick" viewBox="0 0 10 10">
      <rect x="1" y="1.5" width="7.5" height="7.5" rx="1" fill="none" stroke="#2f6fc0" stroke-width="1.4"/>
      <path d="M3 5.2 L5 7.2 L9.5 1.5" fill="none" stroke="#2f6fc0" stroke-width="1.6"/>
    </symbol>
    <symbol id="phone" viewBox="0 0 10 10">
      <path d="M2.2 1 L4 2.8 L3 4 Q4.2 6.2 6 7 L7.2 6 L9 7.8 L7.8 9 Q4.5 9 1 5 Q.8 2.5 2.2 1Z" fill="var(--icon)"/>
    </symbol>
    <symbol id="mail" viewBox="0 0 10 10">
      <rect x=".8" y="2.5" width="8.4" height="5.6" rx=".6" fill="var(--icon)"/>
      <path d="M.8 2.8 L5 5.8 L9.2 2.8" fill="none" stroke="#0c75c6" stroke-width=".8"/>
    </symbol>
    <symbol id="globe" viewBox="0 0 10 10">
      <circle cx="5" cy="5" r="4" fill="none" stroke="var(--icon)" stroke-width="1"/>
      <ellipse cx="5" cy="5" rx="1.8" ry="4" fill="none" stroke="var(--icon)" stroke-width=".8"/>
      <path d="M1 5 H9 M1.7 3 H8.3 M1.7 7 H8.3" stroke="var(--icon)" stroke-width=".7"/>
    </symbol>
  </defs>
</svg>

<!-- Front of postcard -->
<section class="card card--front front">
  <div class="front__photo" role="img" aria-label="Black and white photograph of two smiling boys hugging"></div>

  <div class="brand" style="left:31px; top:42px;">
    <span class="brand__dot"></span>
    <span class="brand__name" style="font-size:15px;">Bright Willow Kids</span>
  </div>
  <p class="brand__slogan" style="left:51px; top:64px; font-size:7.6px;">Improving skills and function for daily living</p>

  <h1 class="front__headline">
    <span class="teal">Pediatric Occupational, Physical</span><br>
    <span class="navy">and Speech Therapy Services;</span><br>
    <span class="teal">Assistive Technology Evaluation</span><br>
    <span class="teal">and Training</span>
  </h1>

  <h2 class="front__subhead">Speech-Language Therapy</h2>
  <ul class="skill-list skill-list--a">
    <li><svg class="tick"><use href="#tick"/></svg>Oral motor skills</li>
    <li><svg class="tick"><use href="#tick"/></svg>speech delays</li>
    <li><svg class="tick"><use href="#tick"/></svg>language skills</li>
    <li><svg class="tick"><use href="#tick"/></svg>Articulation</li>
    <li><svg class="tick"><use href="#tick"/></svg>Voice</li>
  </ul>
  <ul class="skill-list skill-list--b">
    <li><svg class="tick"><use href="#tick"/></svg>Fluency</li>
    <li><svg class="tick"><use href="#tick"/></svg>Cognitive skills</li>
    <li><svg class="tick"><use href="#tick"/></svg>Feeding disorders</li>
    <li><svg class="tick"><use href="#tick"/></svg>Play skills</li>
  </ul>

  <p class="cta"><span class="cta__lead">CONTACT US TODAY</span><span class="cta__offer">for a FREE 15 minute consultation/Screen</span></p>

  <div class="contact-band">
    <span class="contact-item"><svg><use href="#phone"/></svg>(301) 555-4182</span>
    <span class="contact-item"><svg><use href="#mail"/></svg>info@brightwillowkids.example</span>
    <span class="contact-item"><svg><use href="#globe"/></svg>www.brightwillowkids.example</span>
  </div>
</section>

<!-- Back of postcard -->
<section class="card card--back back">
  <h2 class="section-tab">OCCUPATIONAL THERAPY</h2>
  <p class="back__intro">Our occupational therapists use play in therapy to help your child develop the skills he/she needs to perform their job of living and playing, including but not limited to:</p>
  <ul class="ot-list">
    <li><svg class="tick"><use href="#tick"/></svg><span>Increasing independence in self-care skills such as feeding, dressing and grooming</span></li>
    <li><svg class="tick"><use href="#tick"/></svg><span>Improving developmental skills such as rolling, sitting, standing</span></li>
    <li><svg class="tick"><use href="#tick"/></svg><span>Improving their sensory processing, balance, coordination and motor planning</span></li>
    <li><svg class="tick"><use href="#tick"/></svg><span>Difficulty tolerating clothing</span></li>
    <li><svg class="tick"><use href="#tick"/></svg><span>Poor balance - doesn't ride a bike/climb on slides, falls frequently, cries when moved unexpectedly</span></li>
    <li><svg class="tick"><use href="#tick"/></svg><span>Intolerance to textures/odors/loud sounds/movement</span></li>
    <li><svg class="tick"><use href="#tick"/></svg><span>Delayed handwriting and fine motor skills and/or avoids fine motor activities such as using crayons, fasteners on clothing, pencils</span></li>
    <li><svg class="tick"><use href="#tick"/></svg><span>Limited diet-refuses to try new foods, gags when trying new tastes, textures</span></li>
    <li><svg class="tick"><use href="#tick"/></svg><span>Appears extremely anxious, states frequent fears of harmless things</span></li>
  </ul>

  <p class="cta"><span class="cta__lead">CONTACT US TODAY</span><span class="cta__offer">for a FREE 15 minute consultation/Screen</span></p>

  <div class="contact-band">
    <div class="row">
      <span class="contact-item"><svg><use href="#phone"/></svg>(301) 555-4182</span>
      <span class="contact-item"><svg><use href="#mail"/></svg>info@brightwillowkids.example</span>
    </div>
    <div class="row">
      <span class="contact-item"><svg><use href="#globe"/></svg>www.brightwillowkids.example</span>
    </div>
  </div>

  <div class="back__divider"></div>

  <div class="brand" style="left:289px; top:42px;">
    <span class="brand__dot" style="width:10px;height:10px;"></span>
    <span class="brand__name" style="font-size:10px;">Bright Willow Kids</span>
  </div>
  <p class="brand__slogan" style="left:305px; top:58px; font-size:5px;">Improving skills and function for daily living</p>

  <div class="stamp-box"></div>
  <div class="address-line" style="top:164px;"></div>
  <div class="address-line" style="top:201px;"></div>
  <div class="address-line" style="top:239px;"></div>
</section>
</body>
</html>
```